Tova Brisk Fitness Coaching Project

I am a personal trainer based in London. My services include one-on-one PT sessions, bootcamps.
I would like the design to be minimalistic. With light colours: white, pink, purple.
I specialise in weight loss, flexibility, mobility.

Tova Penrick
Personal Trainer
Email: tova.penrick@mailgrove.net
tel: 07500 918 243
Instagram: Tova Brisk

Target Market(s)

adults, mostly females (age 18-50).

Industry/Entity Type

Fitness

Contact Information for Business Card

Tova Penrick
Personal Trainer
tel: 07500 918 243
Instagram: Tova Brisk

Font styles to use
Serif

Colors
eea4c8
fbd4d5
fdf9cf
cfeae6
cee9f5

Requirements
Nice to have
• minimalistic style
• easy to read and remember

```html
<!DOCTYPE html>
<html lang="en">
<head>
<meta charset="utf-8">
<title>Tova Brisk Fitness Coaching – Business Card</title>
<link href="https://fonts.googleapis.com/css2?family=Anton&family=Roboto:wght@400;500&display=swap" rel="stylesheet">
<style>
  :root {
    --page-bg: #ecebe9;
    --card-white: #f4f4f4;
    --brand-purple: #7a2f8a;
    --text-grey: #555555;
    --text-dark: #3d3d3d;
    --hot-pink: #ec1a8e;
    --wall-pink: #f0529f;
    --wall-teal: #3fc7cc;
    --deep-teal: #2a9ea6;
    --back-dark: #1c261b;
    --back-green: #2a3a24;
    --back-warm: #8a5238;
    --back-light: #d8c4bc;
    --shadow: rgba(0, 0, 0, 0.28);
  }
  * { box-sizing: border-box; margin: 0; padding: 0; }
  html, body {
    width: 1200px;
    height: 960px;
    overflow: hidden;
    background: var(--page-bg);
  }
  .canvas {
    position: relative;
    width: 1200px;
    height: 960px;
  }
  .card {
    position: absolute;
    width: 600px;
    height: 341px;
    border-radius: 18px;
    overflow: hidden;
    box-shadow: 0 3px 8px var(--shadow);
  }
  .card-front {
    left: 302px;
    top: 130px;
    background: var(--card-white);
  }
  .card-back {
    left: 300px;
    top: 489px;
  }
  .front-photo {
    position: absolute;
    left: 190px;
    top: 0;
    right: 0;
    bottom: 0;
    background: linear-gradient(165deg, var(--hot-pink) 0%, var(--wall-pink) 30%, #b08ab8 45%, var(--wall-teal) 60%, var(--deep-teal) 100%);
    -webkit-mask-image: linear-gradient(to right, transparent 0%, rgba(0,0,0,0.4) 25%, #000 50%);
    mask-image: linear-gradient(to right, transparent 0%, rgba(0,0,0,0.4) 25%, #000 50%);
  }
  .identity {
    position: absolute;
    left: 41px;
    top: 142px;
  }
  .name {
    font-family: "Anton", Impact, sans-serif;
    font-weight: 400;
    font-size: 36px;
    line-height: 1;
    color: var(--brand-purple);
    text-transform: uppercase;
  }
  .role {
    margin-top: 6px;
    font-family: "Roboto", Arial, sans-serif;
    font-weight: 400;
    font-size: 15px;
    color: var(--text-grey);
  }
  .contact-list {
    list-style: none;
    margin-top: 9px;
    font-family: "Roboto", Arial, sans-serif;
    font-size: 14px;
    color: var(--text-dark);
  }
  .contact-item {
    display: flex;
    align-items: center;
    height: 19px;
  }
  .contact-icon {
    width: 13px;
    height: 13px;
    margin-right: 10px;
    flex: none;
  }
  .social-square {
    width: 11px;
    height: 11px;
    margin: 0 11px 0 1px;
    background: var(--brand-purple);
    border-radius: 2px;
    flex: none;
  }
  .services-band {
    position: absolute;
    left: 0;
    top: 280px;
    width: 220px;
    height: 29px;
    background: var(--brand-purple);
    color: #ffffff;
    font-family: "Roboto", Arial, sans-serif;
    font-size: 14px;
    line-height: 29px;
    padding-left: 41px;
  }
  .back-photo {
    position: absolute;
    inset: 0;
    background: linear-gradient(115deg, var(--back-dark) 0%, var(--back-green) 25%, var(--back-warm) 50%, #6b4030 68%, var(--back-light) 88%, var(--back-dark) 100%);
  }
</style>
</head>
<body>
<main class="canvas">
  <section class="card card-front">
    <div class="front-photo" role="img" aria-label="Photo of the trainer leaping in a pink hoodie in front of a pink and teal painted wall"></div>
    <div class="identity">
      <h1 class="name">Tova Penrick</h1>
      <p class="role">Personal Trainer</p>
      <ul class="contact-list">
        <li class="contact-item">
          <svg class="contact-icon" viewBox="0 0 24 24" aria-hidden="true"><path fill="#7a2f8a" d="M6.6 10.8a15.1 15.1 0 0 0 6.6 6.6l2.2-2.2c.3-.3.7-.4 1-.2 1.1.4 2.3.6 3.6.6.6 0 1 .4 1 1V20c0 .6-.4 1-1 1A17 17 0 0 1 3 4c0-.6.4-1 1-1h3.5c.6 0 1 .4 1 1 0 1.3.2 2.5.6 3.6.1.3 0 .7-.2 1z"/></svg>
          <span>07500 918 243</span>
        </li>
        <li class="contact-item">
          <svg class="contact-icon" viewBox="0 0 24 24" aria-hidden="true"><path fill="#7a2f8a" d="M3 5h18v14H3z"/><path fill="none" stroke="#f4f4f4" stroke-width="1.8" d="M3.5 6l8.5 7 8.5-7"/></svg>
          <span>tova.penrick@mailgrove.net</span>
        </li>
        <li class="contact-item">
          <span class="social-square" aria-hidden="true"></span>
          <span>Tova Brisk</span>
        </li>
      </ul>
    </div>
    <div class="services-band">PT sessions, bootcamps.</div>
  </section>

  <section class="card card-back">
    <div class="back-photo" role="img" aria-label="Portrait photo of the trainer with curly hair in a floral blouse against a dark green background"></div>
  </section>
</main>
</body>
</html>
```